Quenby Computers Customer Acquisition Flyer

I need a flyer design for Quenby Computers which is aimed at acquiring new customers. They will be distributed in a letterbox drop and as handouts.

The design should communicate our ability to aid both consumer and small business with all their IT needs and wants, that we have all tools and skills to assist them. It would look modern, professional with a design on the bolder side of the scale.

Very little text to go on flyer, its more about letting people know who we are, wand what we do.

We do:
Computer hardware / software installation and troubleshooting
Custom built computers
Internet installations / WiFi set up
Network installation and consultation
Computer IT Security
Cloud Computing experts
Certified Torvan phone technicians.

not all of that needs to be on flyer, but if is an computer or connected to a computer / network, we can help you.

I have no preference on colours apart from logo which should not be changed.

If anyone require any more information to create a flyer, just ask me, as i am not sure how much information is needed.

Flyer should be in A5 format.

Target Market(s)

consumer and small business (1-50 employees)

Industry/Entity Type

Computer Repair

Requirements
Must have
• Clear easy to read text, graphics that convey us as the professionals we are.
• Logo with tag line, Your local IT specialists
• Contact details:
• Mobile: 0479 612 304
• Email: support@quenbycomputers.com.au
• Web: www.quenbycomputers.com.au
• Be in A5 format
Nice to have
• contact details like mobile to really stand out along with logo.
Should not have
• Go wild, you should not restrict too much the creative people out there.

```html
<!DOCTYPE html>
<html lang="en">
<head>
<meta charset="utf-8">
<title>Quenby Computers – Your Local IT Specialists</title>
<link rel="stylesheet" href="https://fonts.googleapis.com/css2?family=Oswald:wght@400;500;700&family=Roboto:wght@400;500&display=swap">
<style>
  :root {
    --brand-red: #d7141c;
    --deep-red: #a80d13;
    --ink: #161616;
    --charcoal: #2b2b2d;
    --paper: #ffffff;
  }
  html, body {
    margin: 0;
    padding: 0;
    width: 900px;
    height: 1200px;
    overflow: hidden;
    background: var(--paper);
  }
  .flyer {
    position: relative;
    width: 900px;
    height: 1200px;
    overflow: hidden;
    background: var(--paper);
    font-family: "Roboto", Arial, sans-serif;
    color: var(--ink);
  }
  .flyer__shapes {
    position: absolute;
    inset: 0;
  }
  .hero-visual {
    position: absolute;
    left: 620px;
    top: 30px;
    width: 260px;
    height: 500px;
    border-radius: 46% 46% 24% 24%;
    background: radial-gradient(circle at 55% 22%, #5d86b5 0%, #2f4f74 28%, #7b7d82 55%, #3a3b3e 85%);
  }
  .brand {
    position: absolute;
    left: 60px;
    top: 62px;
    display: flex;
    align-items: center;
    gap: 12px;
    z-index: 2;
  }
  .brand__dot {
    width: 20px;
    height: 20px;
    border-radius: 50%;
    background: var(--brand-red);
  }
  .brand__name {
    font-family: "Oswald", Arial, sans-serif;
    font-weight: 700;
    font-size: 42px;
    letter-spacing: 1px;
    text-transform: uppercase;
    color: var(--brand-red);
    line-height: 1;
  }
  .tagline {
    position: absolute;
    left: 60px;
    top: 190px;
    margin: 0;
    font-family: "Oswald", Arial, sans-serif;
    font-size: 70px;
    line-height: 1.02;
    text-transform: uppercase;
    color: var(--ink);
    z-index: 2;
  }
  .tagline__strong { font-weight: 700; display: block; }
  .tagline__light { font-weight: 400; display: block; }
  .services {
    position: absolute;
    left: 60px;
    top: 362px;
    width: 480px;
    z-index: 2;
  }
  .services__title {
    display: flex;
    align-items: center;
    gap: 16px;
    height: 48px;
    width: 270px;
    padding-left: 60px;
    margin: 0 0 12px -60px;
    background: var(--ink);
    color: var(--paper);
    font-family: "Oswald", Arial, sans-serif;
    font-weight: 500;
    font-size: 30px;
    letter-spacing: 1px;
    text-transform: uppercase;
  }
  .services__title svg { flex: none; }
  .services__list {
    list-style: none;
    margin: 0;
    padding: 0;
  }
  .services__item {
    display: flex;
    align-items: flex-start;
    gap: 12px;
    font-size: 20px;
    line-height: 1.25;
    color: var(--ink);
    margin-bottom: 3px;
  }
  .services__item svg {
    flex: none;
    margin-top: 2px;
  }
  .team-photo {
    position: absolute;
    left: 100px;
    top: 680px;
    width: 640px;
    height: 360px;
    background: linear-gradient(160deg, #f4f4f5 0%, #cfd0d2 45%, #8e9094 80%, #6c6e72 100%);
    -webkit-mask-image: linear-gradient(to right, transparent 0%, #000 18%, #000 85%, transparent 100%);
            mask-image: linear-gradient(to right, transparent 0%, #000 18%, #000 85%, transparent 100%);
  }
  .contact {
    position: absolute;
    right: 50px;
    bottom: 30px;
    text-align: right;
    color: var(--paper);
    z-index: 2;
  }
  .contact__phone {
    display: flex;
    align-items: center;
    justify-content: flex-end;
    gap: 14px;
    font-weight: 500;
    font-size: 46px;
    letter-spacing: 1px;
    margin-bottom: 22px;
  }
  .contact__links {
    display: flex;
    gap: 34px;
    font-size: 19px;
  }
  .contact__link {
    display: flex;
    align-items: center;
    gap: 8px;
  }
</style>
</head>
<body>
<main class="flyer">
  <svg class="flyer__shapes" width="900" height="1200" viewBox="0 0 900 1200" aria-hidden="true">
    <path d="M900 220 C760 300 650 420 660 560 C670 700 790 820 900 860 Z" fill="var(--charcoal)"/>
    <path d="M0 1110 C220 1060 420 1010 560 1000 C700 990 820 960 900 900 L900 1200 L0 1200 Z" fill="var(--charcoal)"/>
    <path d="M480 0 C640 90 700 200 640 360 C580 520 610 720 760 860 C820 915 870 930 900 930 L900 960 C830 980 760 1000 640 1010 C520 1020 380 1060 250 1110 C420 1040 560 990 660 940 C560 840 520 660 580 470 C630 310 620 170 430 0 Z" fill="var(--brand-red)"/>
    <path d="M430 0 C620 170 630 310 580 470 C560 540 555 610 565 680 C560 600 575 520 600 450 C650 300 620 150 470 0 Z" fill="var(--deep-red)"/>
  </svg>

  <div class="hero-visual" role="img" aria-label="Robotic hand holding up a globe of the Earth"></div>

  <header class="brand">
    <span class="brand__dot"></span>
    <span class="brand__name">Quenby Computers</span>
  </header>

  <h1 class="tagline"><span class="tagline__strong">Your local</span><span class="tagline__light">IT specialists</span></h1>

  <section class="services">
    <h2 class="services__title">
      <svg width="24" height="24" viewBox="0 0 24 24" aria-hidden="true"><circle cx="12" cy="12" r="12" fill="var(--brand-red)"/><path d="M10 7 L15 12 L10 17" fill="none" stroke="#fff" stroke-width="2.6" stroke-linecap="round" stroke-linejoin="round"/></svg>
      What we do
    </h2>
    <ul class="services__list">
      <li class="services__item"><svg width="20" height="20" viewBox="0 0 22 22" aria-hidden="true"><circle cx="11" cy="11" r="11" fill="var(--brand-red)"/><path d="M6 11.5 L9.5 15 L16 7.5" fill="none" stroke="#fff" stroke-width="2.4" stroke-linecap="round" stroke-linejoin="round"/></svg>Computer hardware / software<br>installation and troubleshooting</li>
      <li class="services__item"><svg width="20" height="20" viewBox="0 0 22 22" aria-hidden="true"><circle cx="11" cy="11" r="11" fill="var(--brand-red)"/><path d="M6 11.5 L9.5 15 L16 7.5" fill="none" stroke="#fff" stroke-width="2.4" stroke-linecap="round" stroke-linejoin="round"/></svg>Custom built computers</li>
      <li class="services__item"><svg width="20" height="20" viewBox="0 0 22 22" aria-hidden="true"><circle cx="11" cy="11" r="11" fill="var(--brand-red)"/><path d="M6 11.5 L9.5 15 L16 7.5" fill="none" stroke="#fff" stroke-width="2.4" stroke-linecap="round" stroke-linejoin="round"/></svg>Internet installations / WiFi set up</li>
      <li class="services__item"><svg width="20" height="20" viewBox="0 0 22 22" aria-hidden="true"><circle cx="11" cy="11" r="11" fill="var(--brand-red)"/><path d="M6 11.5 L9.5 15 L16 7.5" fill="none" stroke="#fff" stroke-width="2.4" stroke-linecap="round" stroke-linejoin="round"/></svg>Network installation and consultation</li>
      <li class="services__item"><svg width="20" height="20" viewBox="0 0 22 22" aria-hidden="true"><circle cx="11" cy="11" r="11" fill="var(--brand-red)"/><path d="M6 11.5 L9.5 15 L16 7.5" fill="none" stroke="#fff" stroke-width="2.4" stroke-linecap="round" stroke-linejoin="round"/></svg>Computer IT Security</li>
      <li class="services__item"><svg width="20" height="20" viewBox="0 0 22 22" aria-hidden="true"><circle cx="11" cy="11" r="11" fill="var(--brand-red)"/><path d="M6 11.5 L9.5 15 L16 7.5" fill="none" stroke="#fff" stroke-width="2.4" stroke-linecap="round" stroke-linejoin="round"/></svg>Cloud Computing experts</li>
      <li class="services__item"><svg width="20" height="20" viewBox="0 0 22 22" aria-hidden="true"><circle cx="11" cy="11" r="11" fill="var(--brand-red)"/><path d="M6 11.5 L9.5 15 L16 7.5" fill="none" stroke="#fff" stroke-width="2.4" stroke-linecap="round" stroke-linejoin="round"/></svg>Certified Torvan phone technicians.</li>
    </ul>
  </section>

  <div class="team-photo" role="img" aria-label="Black and white photo of a business team gathered around a laptop at an office desk"></div>

  <footer class="contact">
    <div class="contact__phone">
      <svg width="40" height="40" viewBox="0 0 40 40" aria-hidden="true"><circle cx="20" cy="20" r="18" fill="none" stroke="var(--brand-red)" stroke-width="3"/><path d="M14 11 L18 11 L19.5 16 L17 18 C18.2 20.8 19.8 22.4 22.5 23.5 L24.5 21 L29.5 22.5 L29.5 26.5 C29.5 27.8 28.5 28.8 27 28.8 C18.5 28.3 11.7 21.5 11.2 13 C11.2 11.8 12.3 11 14 11 Z" fill="var(--brand-red)"/></svg>
      0479 612 304
    </div>
    <div class="contact__links">
      <span class="contact__link"><svg width="20" height="20" viewBox="0 0 20 20" aria-hidden="true"><circle cx="10" cy="10" r="10" fill="var(--brand-red)"/><rect x="5" y="6.5" width="10" height="7" fill="none" stroke="#fff" stroke-width="1.4"/><path d="M5 6.5 L10 10.5 L15 6.5" fill="none" stroke="#fff" stroke-width="1.4"/></svg>support@quenbycomputers.com.au</span>
      <span class="contact__link"><svg width="20" height="20" viewBox="0 0 20 20" aria-hidden="true"><circle cx="10" cy="10" r="10" fill="var(--brand-red)"/><circle cx="10" cy="10" r="5.5" fill="none" stroke="#fff" stroke-width="1.3"/><path d="M4.5 10 H15.5 M10 4.5 C7.5 7.5 7.5 12.5 10 15.5 C12.5 12.5 12.5 7.5 10 4.5" fill="none" stroke="#fff" stroke-width="1.1"/></svg>www.quenbycomputers.com.au</span>
    </div>
  </footer>
</main>
</body>
</html>
```